College Social website needs a SIMPLE chart design

We need a simple one page website. The website is called "Brev-Onto" a phonetic spelling of the word collage. The site allows users to gain up to date information on the nightlife and social scene of the campus. The site must be able to easily convey several key pieces of information; some type of grid/chart would work well.

This includes:
primary information:
-The name of the bar (about 9 bars on campus)
-The length of the line
-Guy/Girl ratio
-If there is cover (admittance fee) to enter the bar

secondary information:
-how packed/full the bar is
-if there is police raiding the bar
-a way to show more information including drink specials

would prefer a design similar to this page except more colorful/playful/fun: http://m.quillbarrowreg.example/results.php
Updates

Some stylistic tips - the name of the service is called brev onto. a phonetic spelling of collage (http://en.fenwickpedia.example/wiki/Collage). it doesnt need to look like a rainbow, just be exciting, engaging, and vivid.

look at this page for reference: http://www.dravelnook.example/blog/flat-ui-design-showcase/

other than the bar name and drink specials, everything should be presented graphically. All the bar stats are approximations and rough estimates, so you must find a way to present the information as relatives. historical information is not relevant. only the real time stats need to be included. here is a sample:

Bar name: Sample bar
guy/girl ratio: 70/30
line length: short
admittance fee: yes
bar attendance: near full
police raid: no
drink specials:
WINE NIGHT!
$8 BOTTLES OF HALTERMOSS WINE
$8 BOTTLES OF CHAMPAGNE
$2 ZEM GOLD BOTTLES
$2 WELLS

Target Market(s)

target market for the site is 18-21 year olds in college.

Industry/Entity Type

College

Requirements
Must have
• the design MUST be mobile friendly. keep it simple. a flat design would be preferred.
the information must be conveyed in the form of symbols/icons. for instance, a pie chart to show guy/girl ratio.

```html
<!DOCTYPE html>
<html lang="en">
<head>
<meta charset="utf-8">
<title>Brev-Onto</title>
<link rel="stylesheet" href="https://fonts.googleapis.com/css2?family=Josefin+Sans:wght@300;400&display=swap">
<style>
  :root{
    --blue:#00bff3;
    --red:#e0401f;
    --yellow:#f0e61e;
    --green:#79dd22;
    --grey:#d9d9d9;
    --ink:#111;
    --footer:#e2e2e2;
    --title-font:"Josefin Sans", Arial, sans-serif;
  }
  *{box-sizing:border-box;margin:0;padding:0}
  html,body{width:1113px;height:1200px;overflow:hidden;background:#fff}
  body{position:relative;font-family:var(--title-font);color:var(--ink)}

  .site-header{position:absolute;left:0;top:0;width:1113px;height:115px}
  .site-header .crowd{position:absolute;inset:0 0 6px 0;
    background:radial-gradient(ellipse at 55% 20%,#d9a5f2 0%,#8f5fc0 18%,transparent 45%),
               linear-gradient(90deg,#1c4a55 0%,#3a8591 30%,#4b5e87 55%,#3a7a88 80%,#1f3c46 100%)}
  .site-header .brand{position:absolute;left:0;right:0;top:28px;text-align:center;color:#fff;
    font-weight:300;font-size:46px;letter-spacing:1px}
  .site-header::after{content:"";position:absolute;left:0;bottom:0;width:100%;height:6px;background:var(--blue)}

  .tile{position:absolute;width:33px;height:33px;display:block}
  .red{background:var(--red)} .yellow{background:var(--yellow)} .green{background:var(--green)}
  .blue{background:var(--blue)} .grey{background:var(--grey)}
  .tile svg{width:33px;height:33px;display:block}
  .fee-mark,.police-mark{color:#fff;text-align:center;font-family:Arial,sans-serif}
  .fee-mark{font-size:24px;line-height:33px}
  .police-mark{font-size:14px;line-height:33px;letter-spacing:2px;font-family:var(--title-font);font-weight:300}

  .legend{position:absolute;left:0;top:160px;width:1113px;height:135px}
  .legend h2{position:absolute;left:72px;top:8px;font-weight:300;font-size:24px}
  .legend .item{position:absolute;font-size:9.5px;line-height:33px;padding-left:40px;height:33px;white-space:nowrap}
  .legend .item .tile{left:0;top:0}
  .legend .divider{position:absolute;width:1px;height:33px;background:#222}

  .bars{position:absolute;left:73px;top:338px;width:967px}
  .bar-row{position:relative;height:81px;border-top:1px solid var(--blue)}
  .bar-row::before{content:"";position:absolute;left:0;top:0;width:100%;height:12px;
    background:radial-gradient(ellipse at 50% 0%,rgba(0,0,0,.45) 0%,rgba(0,0,0,.15) 45%,transparent 70%)}
  .bar-row .pin{position:absolute;left:10px;top:18px;width:26px;height:46px}
  .bar-row .name{position:absolute;left:47px;top:18px;font-weight:300;font-size:27px;line-height:24px}
  .bar-row .addr{position:absolute;left:48px;top:43px;color:var(--blue);font-weight:300;font-size:13px;line-height:13px}
  .bar-row .tile{top:23px}
  .bar-row .divider{position:absolute;top:22px;width:1px;height:36px;background:#222}
  .c-line{left:177px} .c-ratio{left:316px} .c-fee{left:458px} .c-crowd{left:604px} .c-police{left:750px}
  .d1{left:263px} .d2{left:403px} .d3{left:546px} .d4{left:694px}
  .more-info{position:absolute;left:848px;top:25px;font-weight:300;font-size:18px;line-height:30px;display:flex;align-items:center;gap:4px;white-space:nowrap}
  .more-info svg{width:20px;height:28px}

  .ellipsis{position:absolute;left:0;width:1113px;top:1053px;text-align:center;font-size:18px;font-weight:700;letter-spacing:1px}
  .load-more{position:absolute;left:0;top:1080px;width:1113px;height:36px;background:var(--blue);color:#fff;
    text-align:center;font-weight:300;font-size:24px;line-height:40px}

  .site-footer{position:absolute;left:0;top:1116px;width:1113px;height:84px;background:var(--footer)}
  .site-footer h3{position:absolute;left:72px;top:32px;font-weight:300;font-size:24px}
  .social{position:absolute;left:240px;top:34px;display:flex;gap:14px;font-size:13px;line-height:26px}
  .social span{display:flex;align-items:center;gap:5px}
  .social i{display:block;width:12px;height:12px;background:var(--blue)}
  .copyright{position:absolute;right:73px;top:43px;font-family:Arial,sans-serif;font-size:10.5px}
</style>
</head>
<body>

<svg width="0" height="0" style="position:absolute" aria-hidden="true">
  <defs>
    <symbol id="line-long" viewBox="0 0 33 33"><g stroke="#fff" stroke-width="1.6" stroke-linecap="round">
      <path d="M8 9l1 3M11 8l1 3M14 8l1 3M17 9l1 3M20 11l2 2M22 14l3 1M23 17l3 1M23 20l3 1M22 23l3 1"/></g></symbol>
    <symbol id="line-moderate" viewBox="0 0 33 33"><g stroke="#fff" stroke-width="1.6" stroke-linecap="round">
      <path d="M8 9l1 3M11 8l1 3M14 8l1 3M17 9l1 3M20 11l2 2"/></g></symbol>
    <symbol id="line-short" viewBox="0 0 33 33"><g stroke="#fff" stroke-width="1.6" stroke-linecap="round">
      <path d="M8 8l1 3M11 8l1 3"/></g></symbol>
    <symbol id="person" viewBox="0 0 33 33"><g fill="#fff">
      <circle cx="16.5" cy="11" r="2.2"/><rect x="14" y="14" width="5" height="6" rx="1.5"/><rect x="14.6" y="19" width="1.6" height="5"/><rect x="16.8" y="19" width="1.6" height="5"/></g></symbol>
    <symbol id="person-girl" viewBox="0 0 33 33"><g fill="#fff">
      <circle cx="16.5" cy="11" r="2.2"/><path d="M15 14h3l2 7h-7z"/><rect x="14.8" y="20" width="1.4" height="4"/><rect x="16.8" y="20" width="1.4" height="4"/></g></symbol>
    <symbol id="ratio-equal" viewBox="0 0 33 33"><g fill="#fff">
      <circle cx="9" cy="10" r="2"/><rect x="7" y="13" width="4" height="6" rx="1"/><rect x="7.4" y="18" width="1.3" height="5"/><rect x="9.3" y="18" width="1.3" height="5"/>
      <path d="M15 24l3-15" stroke="#fff" stroke-width="1.3"/>
      <circle cx="24" cy="10" r="2"/><path d="M22.5 13h3l2 7h-7z"/><rect x="22.4" y="19" width="1.3" height="4"/><rect x="24.3" y="19" width="1.3" height="4"/></g></symbol>
    <symbol id="crowd-low" viewBox="0 0 33 33"><rect x="4.5" y="13" width="24" height="7" rx="3.5" fill="none" stroke="#fff" stroke-width="1.3"/><rect x="5.5" y="14" width="6" height="5" rx="2.5" fill="#fff"/></symbol>
    <symbol id="crowd-medium" viewBox="0 0 33 33"><rect x="4.5" y="13" width="24" height="7" rx="3.5" fill="none" stroke="#fff" stroke-width="1.3"/><rect x="5.5" y="14" width="12" height="5" rx="2.5" fill="#fff"/></symbol>
    <symbol id="crowd-high" viewBox="0 0 33 33"><rect x="4.5" y="13" width="24" height="7" rx="3.5" fill="none" stroke="#fff" stroke-width="1.3"/><path d="M12 13v7M16.5 13v7M21 13v7" stroke="#fff" stroke-width="1.2"/></symbol>
    <symbol id="map-pin" viewBox="0 0 26 46"><path d="M13 0C5.8 0 0 5.8 0 13c0 9 13 33 13 33s13-24 13-33C26 5.8 20.2 0 13 0z" fill="#000"/><circle cx="13" cy="12" r="5" fill="#fff"/></symbol>
    <symbol id="glass" viewBox="0 0 20 28"><path d="M2 2l8 11 8-11M10 13v12M5 26h10" fill="none" stroke="#000" stroke-width="2.2" stroke-linecap="round"/></symbol>
  </defs>
</svg>

<header class="site-header">
  <div class="crowd" role="img" aria-label="Photo of a crowd dancing under club lights"></div>
  <h1 class="brand">BREV-ONTO</h1>
</header>

<section class="legend">
  <h2>LEGEND:</h2>
  <div class="item" style="left:181px;top:10px"><span class="tile red"><svg><use href="#line-long"/></svg></span>LONG LINE</div>
  <div class="item" style="left:181px;top:52px"><span class="tile yellow"><svg><use href="#line-moderate"/></svg></span>MODERATE LINE</div>
  <div class="item" style="left:181px;top:94px"><span class="tile green"><svg><use href="#line-short"/></svg></span>SHORT LINE</div>
  <span class="divider" style="left:334px;top:10px"></span><span class="divider" style="left:334px;top:52px"></span><span class="divider" style="left:334px;top:94px"></span>

  <div class="item" style="left:364px;top:10px"><span class="tile blue"><svg><use href="#ratio-equal"/></svg></span>APROX. EQUAL</div>
  <div class="item" style="left:364px;top:52px"><span class="tile blue"><svg><use href="#person"/></svg></span>MORE GUYS</div>
  <div class="item" style="left:364px;top:94px"><span class="tile blue"><svg><use href="#person-girl"/></svg></span>MORE GIRLS</div>
  <span class="divider" style="left:500px;top:10px"></span><span class="divider" style="left:500px;top:52px"></span><span class="divider" style="left:500px;top:94px"></span>

  <div class="item" style="left:530px;top:10px"><span class="tile blue fee-mark">$</span>IT IS A FEE</div>
  <div class="item" style="left:530px;top:52px"><span class="tile grey fee-mark">$</span>THERE IS NO FEE</div>
  <span class="divider" style="left:667px;top:10px"></span><span class="divider" style="left:667px;top:52px"></span><span class="divider" style="left:667px;top:94px"></span>

  <div class="item" style="left:698px;top:10px"><span class="tile green"><svg><use href="#crowd-low"/></svg></span>LOW ATTENDANCE</div>
  <div class="item" style="left:698px;top:52px"><span class="tile yellow"><svg><use href="#crowd-medium"/></svg></span>MEDIUM ATTENDANCE</div>
  <div class="item" style="left:698px;top:94px"><span class="tile red"><svg><use href="#crowd-high"/></svg></span>HIGH ATTENDANCE</div>
  <span class="divider" style="left:891px;top:10px"></span><span class="divider" style="left:891px;top:52px"></span><span class="divider" style="left:891px;top:94px"></span>

  <div class="item" style="left:920px;top:10px"><span class="tile blue police-mark">911</span>POLICE PRESENT</div>
  <div class="item" style="left:920px;top:52px"><span class="tile grey police-mark">911</span>POLICE UNPRESENT</div>
</section>

<main class="bars">
  <article class="bar-row">
    <svg class="pin"><use href="#map-pin"/></svg><div class="name">BAR 1</div><div class="addr">ADDRESS<br>NUMBER</div>
    <span class="tile red c-line"><svg><use href="#line-long"/></svg></span><span class="divider d1"></span>
    <span class="tile blue c-ratio"><svg><use href="#person"/></svg></span><span class="divider d2"></span>
    <span class="tile blue fee-mark c-fee">$</span><span class="divider d3"></span>
    <span class="tile yellow c-crowd"><svg><use href="#crowd-medium"/></svg></span><span class="divider d4"></span>
    <span class="tile grey police-mark c-police">911</span>
    <div class="more-info"><svg><use href="#glass"/></svg>MORE INFO...</div>
  </article>
  <article class="bar-row">
    <svg class="pin"><use href="#map-pin"/></svg><div class="name">BAR 2</div><div class="addr">ADDRESS<br>NUMBER</div>
    <span class="tile green c-line"><svg><use href="#line-short"/></svg></span><span class="divider d1"></span>
    <span class="tile blue c-ratio"><svg><use href="#person"/></svg></span><span class="divider d2"></span>
    <span class="tile grey fee-mark c-fee">$</span><span class="divider d3"></span>
    <span class="tile yellow c-crowd"><svg><use href="#crowd-medium"/></svg></span><span class="divider d4"></span>
    <span class="tile grey police-mark c-police">911</span>
    <div class="more-info"><svg><use href="#glass"/></svg>MORE INFO...</div>
  </article>
  <article class="bar-row">
    <svg class="pin"><use href="#map-pin"/></svg><div class="name">BAR 3</div><div class="addr">ADDRESS<br>NUMBER</div>
    <span class="tile green c-line"><svg><use href="#line-short"/></svg></span><span class="divider d1"></span>
    <span class="tile blue c-ratio"><svg><use href="#person"/></svg></span><span class="divider d2"></span>
    <span class="tile grey fee-mark c-fee">$</span><span class="divider d3"></span>
    <span class="tile yellow c-crowd"><svg><use href="#crowd-medium"/></svg></span><span class="divider d4"></span>
    <span class="tile blue police-mark c-police">911</span>
    <div class="more-info"><svg><use href="#glass"/></svg>MORE INFO...</div>
  </article>
  <article class="bar-row">
    <svg class="pin"><use href="#map-pin"/></svg><div class="name">BAR 4</div><div class="addr">ADDRESS<br>NUMBER</div>
    <span class="tile red c-line"><svg><use href="#line-long"/></svg></span><span class="divider d1"></span>
    <span class="tile blue c-ratio"><svg><use href="#person"/></svg></span><span class="divider d2"></span>
    <span class="tile blue fee-mark c-fee">$</span><span class="divider d3"></span>
    <span class="tile yellow c-crowd"><svg><use href="#crowd-medium"/></svg></span><span class="divider d4"></span>
    <span class="tile grey police-mark c-police">911</span>
    <div class="more-info"><svg><use href="#glass"/></svg>MORE INFO...</div>
  </article>
  <article class="bar-row">
    <svg class="pin"><use href="#map-pin"/></svg><div class="name">BAR 5</div><div class="addr">ADDRESS<br>NUMBER</div>
    <span class="tile red c-line"><svg><use href="#line-long"/></svg></span><span class="divider d1"></span>
    <span class="tile blue c-ratio"><svg><use href="#person"/></svg></span><span class="divider d2"></span>
    <span class="tile blue fee-mark c-fee">$</span><span class="divider d3"></span>
    <span class="tile red c-crowd"><svg><use href="#crowd-high"/></svg></span><span class="divider d4"></span>
    <span class="tile grey police-mark c-police">911</span>
    <div class="more-info"><svg><use href="#glass"/></svg>MORE INFO...</div>
  </article>
  <article class="bar-row">
    <svg class="pin"><use href="#map-pin"/></svg><div class="name">BAR 6</div><div class="addr">ADDRESS<br>NUMBER</div>
    <span class="tile red c-line"><svg><use href="#line-long"/></svg></span><span class="divider d1"></span>
    <span class="tile blue c-ratio"><svg><use href="#ratio-equal"/></svg></span><span class="divider d2"></span>
    <span class="tile blue fee-mark c-fee">$</span><span class="divider d3"></span>
    <span class="tile yellow c-crowd"><svg><use href="#crowd-medium"/></svg></span><span class="divider d4"></span>
    <span class="tile grey police-mark c-police">911</span>
    <div class="more-info"><svg><use href="#glass"/></svg>MORE INFO...</div>
  </article>
  <article class="bar-row">
    <svg class="pin"><use href="#map-pin"/></svg><div class="name">BAR 7</div><div class="addr">ADDRESS<br>NUMBER</div>
    <span class="tile red c-line"><svg><use href="#line-long"/></svg></span><span class="divider d1"></span>
    <span class="tile blue c-ratio"><svg><use href="#person"/></svg></span><span class="divider d2"></span>
    <span class="tile blue fee-mark c-fee">$</span><span class="divider d3"></span>
    <span class="tile green c-crowd"><svg><use href="#crowd-low"/></svg></span><span class="divider d4"></span>
    <span class="tile grey police-mark c-police">911</span>
    <div class="more-info"><svg><use href="#glass"/></svg>MORE INFO...</div>
  </article>
  <article class="bar-row">
    <svg class="pin"><use href="#map-pin"/></svg><div class="name">BAR 8</div><div class="addr">ADDRESS<br>NUMBER</div>
    <span class="tile green c-line"><svg><use href="#line-short"/></svg></span><span class="divider d1"></span>
    <span class="tile blue c-ratio"><svg><use href="#person"/></svg></span><span class="divider d2"></span>
    <span class="tile grey fee-mark c-fee">$</span><span class="divider d3"></span>
    <span class="tile yellow c-crowd"><svg><use href="#crowd-medium"/></svg></span><span class="divider d4"></span>
    <span class="tile grey police-mark c-police">911</span>
    <div class="more-info"><svg><use href="#glass"/></svg>MORE INFO...</div>
  </article>
  <article class="bar-row">
    <svg class="pin"><use href="#map-pin"/></svg><div class="name">BAR 9</div><div class="addr">ADDRESS<br>NUMBER</div>
    <span class="tile red c-line"><svg><use href="#line-long"/></svg></span><span class="divider d1"></span>
    <span class="tile blue c-ratio"><svg><use href="#person"/></svg></span><span class="divider d2"></span>
    <span class="tile blue fee-mark c-fee">$</span><span class="divider d3"></span>
    <span class="tile yellow c-crowd"><svg><use href="#crowd-medium"/></svg></span><span class="divider d4"></span>
    <span class="tile grey police-mark c-police">911</span>
    <div class="more-info"><svg><use href="#glass"/></svg>MORE INFO...</div>
  </article>
</main>

<div class="ellipsis">...</div>
<div class="load-more">LOAD MORE</div>

<footer class="site-footer">
  <h3>CONTACT US:</h3>
  <div class="social">
    <span><i></i>Murmur</span>
    <span><i></i>Gatherly</span>
    <span><i></i>Workweb</span>
    <span><i></i>Orbitly</span>
  </div>
  <div class="copyright">© 2013 BREV-ONTO</div>
</footer>

</body>
</html>
```